Business Card Design for Small Electrical Contractor

I need to update my business card into something a little more modern. We are a small electrical contracting company. We service domestic and commercial places around Sydney. We have 2 logo designs at the moment. I have uploaded both and 2 different sizes to work with.

Industry/Entity Type

Business

Contact Information for Business Card

Leo Hartigan
8/21-23 Birch Rd, Kelsworth 2087
t - (02) 9381 4720
m - 0427 815 903
E - info@hartiganelx.com.au
W - hartiganelx.com.au
ABN: 42 907 551 316

Font styles to use
Sans Serif

Requirements
Must have
• I would also like to see the below fit on somewhere aswell
• - Licensed Electrician
• - Level 2 (Cat 1 & 4)
• - Domestic
• - Commercial
• - Repairs and Installations
• - Data
Nice to have
• Try and keep similar colours as logo
Should not have
• No lightning bolts or light globes. Smart and professional please.

```html
<!DOCTYPE html>
<html lang="en">
<head>
<meta charset="utf-8">
<title>Hartigan Electrical – Business Card</title>
<link href="https://fonts.googleapis.com/css2?family=Noto+Serif:wght@700&family=Open+Sans:ital,wght@0,600;0,700;1,600;1,700&display=swap" rel="stylesheet">
<style>
  :root {
    --page-bg: #ebe7e2;
    --card-orange: #e8952e;
    --card-white: #f4f4f4;
    --brand-dark: #1f3a3a;
    --accent: #f0931f;
    --divider: #d6d6d6;
    --icon-grey: #9a9a9a;
    --name-white: #ffffff;
  }
  * { margin: 0; padding: 0; box-sizing: border-box; }
  html, body {
    width: 1029px;
    height: 1200px;
    overflow: hidden;
    background: var(--page-bg);
  }
  .canvas { position: relative; width: 1029px; height: 1200px; }

  .card {
    position: absolute;
    left: 161px;
    width: 732px;
    height: 398px;
  }
  .card--front { top: 163px; background: var(--card-orange); }
  .card--back { top: 635px; background: var(--card-white); }

  .brand {
    position: absolute;
    display: flex;
    align-items: center;
    gap: 14px;
    font-family: "Open Sans", sans-serif;
    font-weight: 700;
    color: var(--brand-dark);
    line-height: 1.05;
  }
  .brand__mark {
    width: 16px;
    height: 16px;
    background: var(--brand-dark);
    flex: none;
  }
  .card--front .brand {
    top: 58px;
    left: 0;
    right: 0;
    justify-content: center;
    font-size: 48px;
  }
  .card--back .brand {
    top: 122px;
    left: 34px;
    width: 300px;
    font-size: 44px;
  }
  .brand__name { display: block; }

  .holder-name {
    position: absolute;
    top: 176px;
    left: 0;
    right: 0;
    text-align: center;
    font-family: "Noto Serif", serif;
    font-weight: 700;
    font-size: 64px;
    line-height: 1.3;
    letter-spacing: 1px;
    color: var(--name-white);
  }

  .services {
    position: absolute;
    top: 292px;
    left: 0;
    right: 0;
    text-align: center;
    font-family: "Open Sans", sans-serif;
    font-weight: 600;
    font-size: 17px;
    line-height: 1.6;
    color: var(--brand-dark);
    list-style: none;
  }

  .divider {
    position: absolute;
    left: 351px;
    top: 79px;
    width: 1px;
    height: 225px;
    background: var(--divider);
  }

  .contact-list {
    position: absolute;
    left: 370px;
    top: 116px;
    list-style: none;
    font-family: "Open Sans", sans-serif;
    font-style: italic;
    color: var(--accent);
  }
  .contact-item {
    display: flex;
    align-items: center;
    gap: 14px;
  }
  .contact-item svg { width: 16px; height: 18px; flex: none; }
  .contact-item--phone { font-size: 37px; font-weight: 700; height: 46px; }
  .contact-item--email { font-size: 19px; font-weight: 600; height: 32px; }

  .address {
    position: absolute;
    top: 304px;
    left: 0;
    right: 0;
    text-align: center;
    font-family: "Open Sans", sans-serif;
    font-style: italic;
    font-weight: 600;
    font-size: 21px;
    color: var(--accent);
  }
  .abn {
    position: absolute;
    top: 349px;
    right: 20px;
    font-family: "Open Sans", sans-serif;
    font-style: italic;
    font-weight: 600;
    font-size: 19px;
    letter-spacing: 0.5px;
    color: var(--accent);
  }
</style>
</head>
<body>
<div class="canvas">

  <section class="card card--front">
    <div class="brand">
      <span class="brand__mark"></span>
      <span class="brand__name">Hartigan Electrical</span>
    </div>
    <h1 class="holder-name">Leo Hartigan</h1>
    <ul class="services">
      <li>Licensed Electrician · Level 2 (Cat 1 &amp; 4)</li>
      <li>Domestic · Commercial · Repairs and Installations · Data</li>
    </ul>
  </section>

  <section class="card card--back">
    <div class="brand">
      <span class="brand__mark"></span>
      <span>
        <span class="brand__name">Hartigan</span>
        <span class="brand__name">Electrical</span>
      </span>
    </div>

    <div class="divider"></div>

    <ul class="contact-list">
      <li class="contact-item contact-item--phone">
        <svg viewBox="0 0 16 18" aria-hidden="true"><rect x="4" y="1" width="8" height="16" rx="1.5" fill="none" stroke="var(--icon-grey)" stroke-width="1.4"/><line x1="7" y1="14.5" x2="9" y2="14.5" stroke="var(--icon-grey)" stroke-width="1.4"/></svg>
        <span>0427 815 903</span>
      </li>
      <li class="contact-item contact-item--phone">
        <svg viewBox="0 0 16 18" aria-hidden="true"><path d="M6 2 L8 5 L6.5 7 Q7.5 10.5 10 12.5 L12 11 L14 14 L11.5 16 Q4 12 4 3 Z" fill="var(--icon-grey)"/></svg>
        <span>(02) 9381 4720</span>
      </li>
      <li class="contact-item contact-item--email">
        <svg viewBox="0 0 22 16" aria-hidden="true" style="width:22px;height:16px"><rect x="1" y="2" width="20" height="12" fill="none" stroke="var(--icon-grey)" stroke-width="1.3"/><path d="M1 2 L11 9 L21 2 M1 14 L8 7 M21 14 L14 7" fill="none" stroke="var(--icon-grey)" stroke-width="1.3"/></svg>
        <span>info@hartiganelx.com.au</span>
      </li>
      <li class="contact-item contact-item--email">
        <svg viewBox="0 0 22 16" aria-hidden="true" style="width:22px;height:16px"><circle cx="11" cy="8" r="6.5" fill="none" stroke="var(--icon-grey)" stroke-width="1.3"/><ellipse cx="11" cy="8" rx="3" ry="6.5" fill="none" stroke="var(--icon-grey)" stroke-width="1.1"/><line x1="4.5" y1="8" x2="17.5" y2="8" stroke="var(--icon-grey)" stroke-width="1.1"/></svg>
        <span>hartiganelx.com.au</span>
      </li>
    </ul>

    <p class="address">8/21-23 Birch Rd, Kelsworth 2087</p>
    <p class="abn">ABN: 42 907 551 316</p>
  </section>

</div>
</body>
</html>
```